'Pellingham Video' - Website Template Design (that I can use in Word Press)

I would like a professional, colorful website template (4 pages) designed in a format that can be used with Word Press. Upon completion of the design, I would like to take over and maintain/host using Web Press and my Go Daddy account.

My business is videography - producing videos for companies, organizations and not-for-profit charities. Our company will do everything, including writing, planning, producing, directing filming and editing videos etc.

I have a colorful logo and business card already designed and I would like the website built around the look of the logo and business card.

I would like an index page designed first. Once the designer has created an index page I like best, I would like three more pages created with that same design.

1) A 'contact us' page
2) A page with a plug in that would allow me to upload video or connect to YouTube to show samples of my videography
3) A general template page I could add new pages to in the future.

Target Market(s)

businesses of all kinds, organizations, governments, not-for-profit charities

Industry/Entity Type

Film Production

Number of Pages Required

4 page

Font styles to use
Sans Serif

Requirements
Must have
• 1) Index page
• 2) Contact Us page
• 2) A page with a plug in that would allow me to upload video or connect to YouTube to show samples of my videography
• 3) A general template page I could add new pages to in the future
Nice to have
• Surprise me! I love lots of color and am open to creative ideas.

```html
<!DOCTYPE html>
<html lang="en">
<head>
<meta charset="utf-8">
<title>Pellingham Video — Video Production Company</title>
<link href="https://fonts.googleapis.com/css2?family=Montserrat:wght@500;600;700&family=Mulish:wght@400;600;700&display=swap" rel="stylesheet">
<style>
:root{
  --red:#e8202a;
  --orange:#f06a22;
  --purple:#7b3f98;
  --blue:#3a4fa0;
  --green:#a4c93a;
  --yellow:#f0e014;
  --charcoal:#3a3a3a;
  --ink:#1e1e1e;
  --text:#6b6b6b;
  --card-red:#d93a2b;
  --card-green:#5a9e3a;
  --card-purple:#5b2a7a;
  --button:#f5e50e;
  --footer:#333333;
  --footer-base:#2a2a2a;
  --white:#ffffff;
}
*{box-sizing:border-box;margin:0;padding:0}
html,body{width:1200px;height:3232px;overflow:hidden}
body{font-family:"Mulish",sans-serif;color:var(--text);background:var(--white);position:relative}
h1,h2,h3,.brand,.nav a{font-family:"Montserrat",sans-serif}
.abs{position:absolute}

.rainbow{display:flex;height:5px;width:100%}
.rainbow span{flex:1}
.rainbow span:nth-child(1){background:var(--red)}
.rainbow span:nth-child(2){background:var(--orange)}
.rainbow span:nth-child(3){background:var(--purple)}
.rainbow span:nth-child(4){background:var(--blue)}
.rainbow span:nth-child(5){background:var(--green)}
.rainbow span:nth-child(6){background:var(--yellow)}
.rainbow span:nth-child(7){background:var(--charcoal)}

/* header */
.site-header{position:absolute;top:0;left:0;width:1200px;height:151px;background:var(--white)}
.social{display:flex;gap:8px}
.social span{width:26px;height:26px;border-radius:50%;display:block}
.header-social{left:78px;top:65px}
.brand{display:flex;align-items:center;gap:12px;font-weight:700;color:var(--ink);letter-spacing:1px;text-transform:uppercase}
.header-brand{left:0;width:1200px;top:56px;justify-content:center;font-size:30px}
.brand .mark{width:34px;height:34px;background:var(--red);display:block}
.phone{display:flex;align-items:center;gap:10px;color:var(--red);font-size:20px;font-weight:600}
.header-phone{right:52px;top:66px}

.nav{position:absolute;top:151px;left:0;width:1200px;height:56px;display:flex}
.nav a{flex:1;display:flex;align-items:center;justify-content:center;color:var(--white);font-size:14px;font-weight:600;text-transform:uppercase;text-decoration:none}
.nav a:nth-child(1){background:var(--red)}
.nav a:nth-child(2){background:var(--orange)}
.nav a:nth-child(3){background:var(--purple)}
.nav a:nth-child(4){background:var(--blue)}
.nav a:nth-child(5){background:var(--green)}
.nav a:nth-child(6){background:var(--yellow)}
.nav a:nth-child(7){background:var(--charcoal)}

/* hero */
.hero{position:absolute;top:207px;left:0;width:1200px;height:461px;
  background:radial-gradient(circle at 50% 48%,#0b1a2a 0 70px,#1a5a4a 110px,#0f7a3a 170px,#1c3a8a 240px,#0b1030 340px,#05070d 520px)}
.hero h1{position:absolute;top:168px;width:100%;text-align:center;color:var(--white);font-size:42px;font-weight:700;line-height:57px;text-transform:uppercase}
.hero-dots{position:absolute;top:626px;left:0;width:1200px;display:flex;justify-content:center;gap:8px}
.hero-dots span{width:12px;height:12px;border-radius:50%;background:var(--yellow)}

/* section headings */
.section-title{position:absolute;left:0;width:1200px;display:flex;align-items:center;justify-content:center;gap:24px;font-size:23px;font-weight:700;text-transform:uppercase;letter-spacing:.5px}
.section-title::before,.section-title::after{content:"";width:85px;height:2px;background:currentColor}
.section-mark{position:absolute;left:582px;width:36px;height:36px}

/* welcome */
.welcome-mark{top:714px;background:var(--red)}
.welcome-title{top:756px;color:var(--ink)}
.welcome-text{position:absolute;left:75px;top:812px;width:1050px;text-align:center;font-size:16px;line-height:28px}

/* services */
.services{position:absolute;top:974px;left:0;width:1200px;height:646px;
  background:linear-gradient(180deg,#1f1f1f 0,#1f1f1f 270px,#2d4c5a 380px,#1a3c4c 520px,#123040 646px)}
.services-mark{top:1018px;background:var(--yellow)}
.services-title{top:1058px;color:var(--white)}
.service{position:absolute;width:330px;height:207px;color:var(--white);text-align:center;padding-top:30px}
.service svg{display:block;margin:0 auto}
.service h3{font-size:15px;font-weight:700;text-transform:uppercase;margin-top:18px}
.service p{font-size:15px;line-height:25px;margin-top:4px}
.service.red{background:var(--red)}
.service.yellow{background:var(--yellow)}
.service.green{background:var(--green)}
.service.blue{background:var(--blue)}
.service.orange{background:var(--orange)}
.service.purple{background:var(--purple);display:flex;align-items:center;justify-content:center;padding:0}

/* works */
.works{position:absolute;top:1620px;left:0;width:1200px;height:495px;
  background:linear-gradient(160deg,#3a3028 0,#2a2522 35%,#4a3a2e 65%,#1f1c1a 100%)}
.works-mark{top:1674px;background:var(--blue)}
.works-title{top:1715px;color:var(--white)}
.work{position:absolute;top:1792px;width:239px}
.work .thumb{height:194px;border:3px solid #d9d9d9;position:relative}
.work .thumb svg{position:absolute;left:50%;top:50%;transform:translate(-50%,-50%)}
.work p{color:var(--yellow);font-family:"Montserrat",sans-serif;font-size:13px;font-weight:700;text-transform:uppercase;text-align:center;line-height:22px;margin-top:20px}
.arrow{position:absolute;top:1909px}

/* feature cards */
.card{position:absolute;top:2160px;width:330px;height:408px;color:var(--white);text-align:center}
.card.red{background:var(--card-red)}
.card.green{background:var(--card-green)}
.card.purple{background:var(--card-purple)}
.card h2{font-size:24px;font-weight:700;text-transform:uppercase;margin-top:22px}
.card .photo{margin:14px auto 0;width:295px;height:151px}
.card p{font-size:16px;line-height:26px;margin:18px 22px 0}
.card .button{display:block;margin:24px auto 0;width:179px;height:38px;line-height:38px;background:var(--button);color:var(--ink);font-family:"Montserrat",sans-serif;font-size:15px;font-weight:600;text-decoration:none}

/* map */
.map{position:absolute;top:2613px;left:0;width:1200px;height:349px;background:linear-gradient(135deg,#dfe6d4,#e8e4dc 50%,#d6dfcc)}
.map-card{position:absolute;top:2645px;left:75px;width:265px;height:267px;background:var(--white);box-shadow:0 2px 8px rgba(0,0,0,.25);text-align:center;padding-top:32px}
.map-card .brand{justify-content:center;font-size:15px;gap:8px}
.map-card .brand .mark{width:22px;height:22px}
.map-card address{font-style:normal;color:var(--ink);font-size:14px;line-height:25px;margin-top:22px}
.map-card .line{display:flex;align-items:center;justify-content:center;gap:8px;color:var(--red);font-size:14px;line-height:28px}

/* footer */
.footer-strip{position:absolute;top:2957px;left:0}
.site-footer{position:absolute;top:2962px;left:0;width:1200px;height:204px;background:var(--footer);color:#e2e2e2}
.footer-brand{left:75px;top:3002px;color:var(--white);font-size:16px;gap:8px}
.footer-brand .mark{width:28px;height:28px}
.footer-about{position:absolute;left:75px;top:3076px;width:300px;font-size:13px;line-height:24px;color:#cfcfcf}
.site-footer h3,.footer-col h3{font-size:13px;font-weight:700;color:var(--white);text-transform:uppercase}
.footer-col{position:absolute;font-size:13px;line-height:28px;color:#d5d5d5}
.footer-col ul{list-style:none}
.footer-social span{width:28px;height:28px}
.copyright{position:absolute;top:3166px;left:0;width:1200px;height:66px;background:var(--footer-base);color:#9a9a9a;font-size:13px;text-align:center;line-height:66px}
</style>
</head>
<body>

<header class="site-header">
  <div class="rainbow"><span></span><span></span><span></span><span></span><span></span><span></span><span></span></div>
  <div class="social header-social abs">
    <span style="background:#3b5998"></span><span style="background:#1da1f2"></span><span style="background:#444"></span><span style="background:#cb2027"></span><span style="background:#dd4b39"></span><span style="background:#e52d27"></span>
  </div>
  <div class="brand header-brand abs"><span class="mark"></span>Pellingham Video</div>
  <div class="phone header-phone abs">
    <svg width="18" height="18" viewBox="0 0 18 18"><rect width="18" height="18" rx="3" fill="#e8202a"/><path d="M5 4l2 0 1 3-1.5 1a7 7 0 0 0 3.5 3.5L11 10l3 1v2a1 1 0 0 1-1 1A9 9 0 0 1 4 5a1 1 0 0 1 1-1z" fill="#fff"/></svg>
    1-800-555-0142
  </div>
</header>

<nav class="nav">
  <a href="#">Home</a><a href="#">About Us</a><a href="#">Services</a><a href="#">Works</a><a href="#">News &amp; Events</a><a href="#">Blog</a><a href="#">Contact</a>
</nav>

<section class="hero" role="img" aria-label="Close-up of a camera lens glowing green and blue">
  <h1>Welcome to Pellingham Video<br>Production Company</h1>
</section>
<div class="hero-dots"><span></span><span></span><span></span><span></span></div>

<section class="welcome">
  <span class="section-mark welcome-mark"></span>
  <h2 class="section-title welcome-title">Welcome to Pellingham Video</h2>
  <p class="welcome-text">Aliquam molestie, mi et imperdiet euismod, dui purus auctor tellus, et interdum lacus lectus et ante. Sed accumsan sollicitudin sapien, sit amet adipiscing turpis gravida ac. In congue, neque ac lobortis volutpat, libero mauris varius mi, vitae suscipit ipsum ligula vitae risus. Duis aliquam nibh a dui iaculis viverra id a velit. Vivamus egestas risus in magna varius commodo. Sed semper viverra egestas. Etiam pretium porttitor lectus, vel ornare neque porta volutpat.</p>
</section>

<section class="services" role="img" aria-label="Dimmed photo of a film set behind the services grid"></section>
<span class="section-mark services-mark"></span>
<h2 class="section-title services-title">Pellingham Video Services</h2>

<div class="service red" style="left:75px;top:1124px">
  <svg width="50" height="46" viewBox="0 0 50 46" fill="none" stroke="#fff" stroke-width="3"><rect x="4" y="8" width="32" height="32" rx="4"/><path d="M22 28l2-7 18-18 5 5-18 18z" fill="#e8202a"/></svg>
  <h3>Writing</h3><p>Sed accumsan sollicitudin sapien,<br>sit amet adipiscing turpis..</p>
</div>
<div class="service yellow" style="left:435px;top:1124px">
  <svg width="50" height="46" viewBox="0 0 50 46" fill="none" stroke="#fff" stroke-width="3"><rect x="6" y="7" width="38" height="36" rx="3"/><path d="M14 2v9M36 2v9M6 16h38"/><path d="M13 23h5M22 23h5M31 23h5M13 30h5M22 30h5M31 30h5M13 37h5M22 37h5" stroke-width="3.5"/></svg>
  <h3>Planning</h3><p>Sed accumsan sollicitudin sapien,<br>sit amet adipiscing turpis..</p>
</div>
<div class="service green" style="left:795px;top:1124px">
  <svg width="50" height="46" viewBox="0 0 50 46"><rect x="4" y="18" width="42" height="24" fill="#fff"/><path d="M4 6l40-4 2 10-42 4z" fill="#fff"/><path d="M12 5l6 10M22 4l6 10M32 3l6 10" stroke="#a4c93a" stroke-width="3"/></svg>
  <h3>Producing</h3><p>Sed accumsan sollicitudin sapien,<br>sit amet adipiscing turpis..</p>
</div>
<div class="service blue" style="left:75px;top:1361px">
  <svg width="50" height="46" viewBox="0 0 50 46" fill="#fff"><rect x="3" y="10" width="30" height="26" rx="4"/><path d="M35 20l12-8v22l-12-8z"/></svg>
  <h3>Directing Filming</h3><p>Sed accumsan sollicitudin sapien,<br>sit amet adipiscing turpis..</p>
</div>
<div class="service orange" style="left:435px;top:1361px">
  <svg width="50" height="46" viewBox="0 0 50 46" fill="none" stroke="#fff" stroke-width="3"><rect x="4" y="4" width="34" height="26"/><path d="M4 10h34M10 4v6M18 4v6M26 4v6"/><circle cx="30" cy="38" r="4"/><circle cx="42" cy="38" r="4"/><path d="M33 35l10-14M39 35l-10-14"/></svg>
  <h3>Editing Videos</h3><p>Sed accumsan sollicitudin sapien,<br>sit amet adipiscing turpis..</p>
</div>
<div class="service purple" style="left:795px;top:1361px">
  <svg width="40" height="40" viewBox="0 0 40 40"><path d="M20 4v32M4 20h32" stroke="#a57ac0" stroke-width="7"/></svg>
</div>

<section class="works" role="img" aria-label="Film clapperboard and camera gear on a wooden table"></section>
<span class="section-mark works-mark"></span>
<h2 class="section-title works-title">Our Works</h2>

<svg class="arrow" style="left:46px" width="18" height="24" viewBox="0 0 18 24"><path d="M14 2L4 12l10 10" fill="none" stroke="#fff" stroke-width="4"/></svg>
<svg class="arrow" style="left:1140px" width="18" height="24" viewBox="0 0 18 24"><path d="M4 2l10 10L4 22" fill="none" stroke="#fff" stroke-width="4"/></svg>

<div class="work" style="left:78px">
  <div class="thumb" role="img" aria-label="Film crew working on a street set at night" style="background:linear-gradient(160deg,#4a4a52,#22242a 60%,#5a4a3a)"></div>
  <p>Duis aliquam nibh a dui<br>iaculis viverra...</p>
</div>
<div class="work" style="left:345px">
  <div class="thumb" role="img" aria-label="Outdoor shoot on a waterfront at sunset" style="background:linear-gradient(180deg,#a9c4d8,#d8c8a8 55%,#5a5048)">
    <svg width="50" height="50" viewBox="0 0 50 50"><circle cx="25" cy="25" r="22" fill="none" stroke="#fff" stroke-width="3"/><path d="M20 15l14 10-14 10z" fill="#fff"/></svg>
  </div>
  <p>Duis aliquam nibh a dui<br>iaculis viverra...</p>
</div>
<div class="work" style="left:616px">
  <div class="thumb" role="img" aria-label="Camera operator filming in the city" style="background:linear-gradient(160deg,#8fa6bf,#3a4658 55%,#1d2430)"></div>
  <p>Duis aliquam nibh a dui<br>iaculis viverra...</p>
</div>
<div class="work" style="left:883px">
  <div class="thumb" role="img" aria-label="Presenters in a green screen studio" style="background:linear-gradient(160deg,#2f7a3a,#1f5a2c 55%,#2a2a2a)">
    <svg width="50" height="50" viewBox="0 0 50 50"><circle cx="25" cy="25" r="22" fill="none" stroke="#fff" stroke-width="3"/><path d="M20 15l14 10-14 10z" fill="#fff"/></svg>
  </div>
  <p>Duis aliquam nibh a dui<br>iaculis viverra...</p>
</div>

<article class="card red" style="left:75px">
  <h2>Careers</h2>
  <div class="photo" role="img" aria-label="Two crew members working with a video camera" style="background:linear-gradient(135deg,#f2f2f2,#b8b8b8 50%,#6a5a50)"></div>
  <p>Aliquam molestie, mi et imperdiet euismod, dui purus auctor tellus, et interdum lacus lectus et ante.</p>
  <a class="button" href="#">View Opening</a>
</article>
<article class="card green" style="left:435px">
  <h2>News &amp; Events</h2>
  <div class="photo" role="img" aria-label="Concert stage lit in pink and blue" style="background:linear-gradient(135deg,#1a1a4a,#8a3a9a 50%,#2a3a8a)"></div>
  <p>Aliquam molestie, mi et imperdiet euismod, dui purus auctor tellus, et interdum lacus lectus et ante.</p>
  <a class="button" href="#">View All Events</a>
</article>
<article class="card purple" style="left:795px">
  <h2>Charities</h2>
  <div class="photo" role="img" aria-label="Volunteers joining hands in a circle" style="background:linear-gradient(135deg,#d8e4ee,#a8b8c8 50%,#7a8a9a)"></div>
  <p>Aliquam molestie, mi et imperdiet euismod, dui purus auctor tellus, et interdum lacus lectus et ante.</p>
  <a class="button" href="#">Donate Now</a>
</article>

<section class="map" role="img" aria-label="Street map of the city around the office location"></section>
<div class="map-card">
  <div class="brand"><span class="mark"></span>Pellingham Video</div>
  <address>42 Ashdown Lane,<br>Kelborough, KB4 7RT</address>
  <div class="line">
    <svg width="14" height="14" viewBox="0 0 18 18"><rect width="18" height="18" rx="3" fill="#e8202a"/><path d="M5 4l2 0 1 3-1.5 1a7 7 0 0 0 3.5 3.5L11 10l3 1v2a1 1 0 0 1-1 1A9 9 0 0 1 4 5a1 1 0 0 1 1-1z" fill="#fff"/></svg>
    1-800-555-0142
  </div>
  <div class="line">
    <svg width="14" height="12" viewBox="0 0 14 12"><rect width="14" height="12" rx="1" fill="#e8202a"/><path d="M1 2l6 5 6-5" fill="none" stroke="#fff" stroke-width="1.5"/></svg>
    info@pellinghamvideo.com
  </div>
</div>

<div class="rainbow footer-strip" style="width:1200px"><span></span><span></span><span></span><span></span><span></span><span></span><span></span></div>
<footer class="site-footer"></footer>
<div class="brand footer-brand abs"><span class="mark"></span>Pellingham Video</div>
<p class="footer-about">Consectetuer adipiscing elit, sed diam nonummy nibh euismod tincidunt ut laoreet dolore magna aliquam erat volut- pat.</p>
<div class="footer-col" style="left:467px;top:3000px">
  <h3>Company</h3>
  <ul><li>Home</li><li>About Us</li><li>Services</li><li>Work</li></ul>
</div>
<div class="footer-col" style="left:601px;top:3028px">
  <ul><li>News &amp; Events</li><li>Blog</li><li>Careers</li><li>Contact Us</li></ul>
</div>
<div class="footer-col" style="left:808px;top:3000px">
  <h3>Connect Us</h3>
  <div class="social footer-social" style="margin-top:24px">
    <span style="background:#3b5998"></span><span style="background:#1da1f2"></span><span style="background:#555"></span><span style="background:#cb2027"></span><span style="background:#dd4b39"></span><span style="background:#e52d27"></span>
  </div>
</div>
<div class="copyright">Copyright © 2016. Pellingham Video All Right Reserved</div>

</body>
</html>
```